Rollup Banner & Flyer für eine Messe "Erfolg durch Innovation"

Wir benötigten für eine Messe einen Roll Up Banner und Flyer zum verteilen. Gerne basierend auf der aktuellen Firmenpräsentation und mit unseren Referenzen.
Im flyer sollen unserer Leistungen (Datenanalyse, Simulation, Optimierung und Webapplikation) dargestellt werden mit einem kleinen Text und einem aussagekräftigen bild. (https://www.kalvento.ch/leistungen/)

Target Market(s)

Industrie

Industry/Entity Type

Simulation

Font styles to use
Sans Serif
Other font styles liked:
• Roboto

Requirements
Must have
• Logo, Referenzen

```html
<!DOCTYPE html>
<html lang="de">
<head>
<meta charset="utf-8">
<title>Kalvento – Flyer</title>
<link href="https://fonts.googleapis.com/css2?family=Poppins:ital,wght@0,400;0,600;0,700;1,700;1,800&display=swap" rel="stylesheet">
<style>
  :root {
    --page: #ffffff;
    --ink: #111111;
    --black: #0d0d0d;
    --lime: #e3e86a;
    --lime-deep: #d3d842;
    --paper: #f1f1f3;
    --rule: #d9d9dc;
    --white: #ffffff;
  }
  * { box-sizing: border-box; margin: 0; padding: 0; }
  html, body { width: 1200px; height: 593px; overflow: hidden; background: var(--page); }
  body { font-family: "Poppins", sans-serif; color: var(--ink); position: relative; }

  .flyer {
    position: absolute; left: 401px; top: 15px;
    width: 397px; height: 562px;
    background: var(--paper);
    overflow: hidden;
    box-shadow: 0 2px 8px rgba(0,0,0,.18);
  }

  .hero-photo {
    position: absolute; left: 0; top: 0; width: 397px; height: 250px;
    background:
      radial-gradient(ellipse at 78% 20%, #3b3a36 0%, transparent 45%),
      radial-gradient(ellipse at 60% 35%, #5a4e34 0%, transparent 22%),
      linear-gradient(180deg, #1a1a1a 0%, #222 55%, #3d3b26 78%, #b9bc55 92%, var(--lime) 100%);
  }

  .brand { position: absolute; left: 17px; top: 22px; display: flex; align-items: center; gap: 7px; }
  .brand-dot { width: 30px; height: 30px; border-radius: 50%; background: var(--lime); }
  .brand-name { font-weight: 700; font-size: 21px; color: var(--lime); letter-spacing: .5px; }

  .headline {
    position: absolute; left: 0; width: 397px; top: 152px; text-align: center;
    font-weight: 800; font-style: italic; font-size: 25px; line-height: 29px;
    color: var(--white); text-shadow: 0 1px 3px rgba(0,0,0,.5);
  }

  .tagline-band { position: absolute; left: 0; top: 221px; width: 397px; height: 91px; }
  .tagline {
    position: absolute; left: 0; width: 397px; top: 227px; text-align: center;
    font-weight: 700; font-size: 8px; line-height: 10px; color: var(--white);
  }

  .rule { position: absolute; left: 0; width: 397px; height: 1px; background: var(--rule); }

  .services-intro { position: absolute; left: 31px; top: 263px; width: 345px; font-size: 7.6px; line-height: 9.6px; }
  .services-intro h2 {
    float: left; margin: -3px 8px 0 0;
    font-weight: 800; font-style: italic; font-size: 16px; line-height: 18px; color: var(--lime-deep);
  }
  .services-intro p + p { margin-top: 9px; clear: both; }

  .service { position: absolute; width: 185px; height: 60px; }
  .service-shot { position: absolute; left: 0; top: 0; width: 46px; height: 52px; }
  .service-shot .accent { position: absolute; left: 0; top: 0; width: 14px; height: 52px; background: var(--lime); }
  .service-shot .screen {
    position: absolute; left: 2px; top: 6px; width: 42px; height: 32px;
    background: linear-gradient(180deg, #fafafa, #dfe3e8); border: 2px solid #222; border-radius: 2px;
  }
  .service-shot .stand { position: absolute; left: 16px; top: 38px; width: 14px; height: 7px; background: #c9c9c9; }
  .service-body { position: absolute; left: 55px; top: 4px; width: 128px; }
  .service-body h3 { font-weight: 800; font-style: italic; font-size: 11.5px; line-height: 13px; color: var(--lime-deep); margin-bottom: 1px; }
  .service-body p { font-size: 6.8px; line-height: 8.6px; }

  .cta-shape { position: absolute; left: 0; top: 486px; width: 397px; height: 42px; }
  .cta {
    position: absolute; left: 0; width: 397px; top: 490px; text-align: center;
  }
  .cta strong { display: block; font-weight: 800; font-style: italic; font-size: 17px; line-height: 20px; }
  .cta span { display: block; font-weight: 700; font-size: 7.6px; line-height: 10px; }

  .contact-bar {
    position: absolute; left: 0; top: 528px; width: 397px; height: 30px; background: var(--black);
    display: flex; justify-content: space-around; align-items: center; padding: 0 26px;
  }
  .contact { display: flex; align-items: center; gap: 4px; color: var(--white); font-size: 8px; }
  .contact svg { width: 10px; height: 10px; }
  .bottom-strip { position: absolute; left: 0; top: 558px; width: 397px; height: 4px; background: var(--lime); }
</style>
</head>
<body>
<main class="flyer">
  <div class="hero-photo" role="img" aria-label="Schachfiguren auf dunklem Brett, eine helle Dame schlägt den dunklen König"></div>

  <div class="brand">
    <span class="brand-dot"></span>
    <span class="brand-name">Kalvento</span>
  </div>

  <h1 class="headline">Ihr nächster Schritt<br>–intelligenter gemacht.</h1>

  <svg class="tagline-band" viewBox="0 0 397 91" aria-hidden="true">
    <rect x="0" y="0" width="397" height="29" fill="var(--lime)"/>
    <polygon points="49,0 349,0 334,29 64,29" fill="var(--black)"/>
    <rect x="0" y="29" width="397" height="62" fill="var(--paper)"/>
  </svg>
  <p class="tagline">Strategische Entscheidungen – unterstützt durch Simulation,<br>optimiert durch Analytik.</p>

  <div class="rule" style="top:258px"></div>

  <section class="services-intro">
    <h2>Leistungen</h2>
    <p>Mit Simulation, Datenanalyse und Optimierung entwickeln wir Lösungen, die komplexe Prozesse sichtbar machen, Varianten vergleichbar machen und bessere Entscheidungen ermöglichen.</p>
    <p>Wir begleiten unsere Kunden vom schnellen Vorprojekt bis zur produktiven Lösung – pragmatisch, technisch stark und immer mit Fokus auf dem Nutzen.</p>
  </section>

  <div class="rule" style="top:332px"></div>

  <article class="service" style="left:19px; top:346px">
    <div class="service-shot"><span class="accent"></span><span class="screen" role="img" aria-label="Bildschirm mit Datenanalyse-Dashboard"></span><span class="stand"></span></div>
    <div class="service-body"><h3>Datenanalyse</h3><p>Datenanalyse macht Prozesse sichtbar, erkennt Muster und schafft eine objektive Grundlage für Entscheidungen.</p></div>
  </article>
  <article class="service" style="left:202px; top:346px">
    <div class="service-shot"><span class="accent"></span><span class="screen" role="img" aria-label="Bildschirm mit Planungsansicht der Optimierung"></span><span class="stand"></span></div>
    <div class="service-body"><h3>Optimierung</h3><p>Optimierung sucht automatisch nach der besten Lösung – sei es bei Planung, Ressourcen, Routen oder Abläufen.</p></div>
  </article>
  <article class="service" style="left:19px; top:413px">
    <div class="service-shot"><span class="accent"></span><span class="screen" role="img" aria-label="Bildschirm mit Kartensimulation"></span><span class="stand"></span></div>
    <div class="service-body"><h3>Simulation</h3><p>Simulation bildet reale Prozesse digital ab, damit Abläufe, Kapazitäten und Varianten risikofrei getestet werden können.</p></div>
  </article>
  <article class="service" style="left:202px; top:413px">
    <div class="service-shot"><span class="accent"></span><span class="screen" role="img" aria-label="Bildschirm mit Webapplikation und Diagrammen"></span><span class="stand"></span></div>
    <div class="service-body"><h3>Webapplikationen</h3><p>Wir entwickeln individuelle Webapplikationen, die Daten, Simulationen und Optimierungen in einem benutzerfreundlichen Tool zusammenführen.</p></div>
  </article>

  <svg class="cta-shape" viewBox="0 0 397 42" aria-hidden="true">
    <polygon points="54,0 343,0 351,30 397,30 397,42 0,42 0,30 46,30" fill="var(--lime)"/>
  </svg>
  <div class="cta">
    <strong>Simulieren Sie Ihren Erfolg.</strong>
    <span>Datenbasierte Entscheidungen beginnen hier.</span>
  </div>

  <footer class="contact-bar">
    <span class="contact">
      <svg viewBox="0 0 10 10" aria-hidden="true"><path d="M2 1 L4 1 L4.6 3 L3.4 4 Q4.3 5.8 6 6.6 L7 5.4 L9 6 L9 8 Q8.5 9 7.5 9 Q1 8.2 1 2.5 Q1 1 2 1Z" fill="var(--lime)"/></svg>
      info@kalvento.ch
    </span>
    <span class="contact">
      <svg viewBox="0 0 10 10" aria-hidden="true"><rect x="0.5" y="2" width="9" height="6" fill="var(--lime)"/><path d="M0.5 2 L5 5.5 L9.5 2" stroke="var(--black)" stroke-width="0.8" fill="none"/></svg>
      +41 44 555 01 23
    </span>
    <span class="contact">
      <svg viewBox="0 0 10 10" aria-hidden="true"><g fill="none" stroke="var(--lime)" stroke-width="0.9"><circle cx="5" cy="5" r="4.2"/><ellipse cx="5" cy="5" rx="1.8" ry="4.2"/><path d="M0.8 5 H9.2 M1.5 2.8 H8.5 M1.5 7.2 H8.5"/></g></svg>
      www.kalvento.ch
    </span>
  </footer>
  <div class="bottom-strip"></div>
</main>
</body>
</html>
```